Update Business Card Design

I'm looking to update my business cards. Attached is a photo of the current design. I like the black side so that does not have to be update. The white side needs to be updated. I want the design to be modern and minimalistic.
I am a lawyer and my firm's website is www.brennoxlegalco.com (for reference).
My firm's logo has a horizontal version (which is on the black side of the card) and a vertical version (on the white side). I would prefer to keep the vertical version on the white side and horizontal version on the black side (the logo files are attached).

I am open to redesigning the black side also. I would like one side to have the horizontal logo and the other to have the vertical logo.

```html
<!DOCTYPE html>
<html lang="en">
<head>
<meta charset="utf-8">
<title>Brennox Legal Co. – Business Card</title>
<link href="https://fonts.googleapis.com/css2?family=Lato:ital,wght@0,400;0,700;0,900;1,400&display=swap" rel="stylesheet">
<style>
  :root {
    --bg: #3a3a3a;
    --card-black: #000000;
    --card-white: #ffffff;
    --accent: #16b8e2;
    --silver: #c9cdd1;
    --ink: #3d3d3d;
    --band-grey: #4a4a4a;
  }
  * { margin: 0; padding: 0; box-sizing: border-box; }
  html, body { width: 1200px; height: 900px; overflow: hidden; }
  body {
    background: radial-gradient(circle at 50% 40%, #4a4a4a 0%, var(--bg) 55%, #222 100%);
    font-family: "Lato", sans-serif;
    position: relative;
  }
  .card {
    position: absolute;
    left: 320px;
    width: 560px;
    height: 320px;
    border-radius: 26px;
    overflow: hidden;
    box-shadow: 0 14px 30px rgba(0,0,0,.5);
  }

  /* Black side – horizontal name lockup */
  .card-front { top: 70px; background: var(--card-black); }
  .front-wordmark {
    position: absolute;
    left: 0; right: 0; top: 82px;
    display: flex; align-items: center; justify-content: center; gap: 18px;
  }
  .front-wordmark .mark-dot {
    width: 22px; height: 22px; border-radius: 50%; background: var(--accent);
  }
  .front-wordmark .firm-name {
    color: var(--accent);
    font-size: 46px; font-weight: 700; letter-spacing: 2px;
  }
  .front-band {
    position: absolute; left: 0; right: 0; top: 232px; height: 44px;
    background: var(--accent);
    border-top: 3px solid var(--silver);
    border-bottom: 3px solid var(--silver);
    display: flex; align-items: center; justify-content: center;
  }
  .front-band .web {
    color: #0a0a0a; font-size: 22px; font-weight: 700; letter-spacing: .5px;
  }

  /* White side – details */
  .card-back { top: 480px; background: var(--card-white); }
  .back-square {
    position: absolute; left: 0; top: 96px; width: 44px; height: 62px;
    background: var(--accent);
  }
  .back-wordmark {
    position: absolute; left: 60px; top: 58px; width: 170px;
    color: var(--accent);
    font-size: 30px; font-weight: 700; line-height: 1.1; letter-spacing: 1px;
  }
  .back-wordmark .mark-square {
    display: block; width: 18px; height: 18px; background: var(--accent); margin-bottom: 12px;
  }
  .back-divider {
    position: absolute; left: 60px; top: 178px; width: 150px; height: 2px; background: var(--ink);
  }
  .contact {
    position: absolute; left: 268px; top: 30px; color: var(--ink);
  }
  .contact .person { font-size: 24px; font-weight: 700; letter-spacing: .5px; }
  .contact .role { color: var(--accent); font-style: italic; font-size: 14px; margin-top: 2px; }
  .contact .row { display: flex; align-items: flex-start; gap: 10px; font-size: 13px; line-height: 1.35; margin-top: 10px; }
  .contact .row.strong { font-weight: 900; font-size: 15px; }
  .contact .rule { width: 150px; height: 2px; background: var(--accent); margin: 12px 0 4px 26px; }
  .icon { flex: none; width: 16px; height: 16px; margin-top: 1px; }
  .back-band {
    position: absolute; left: 170px; right: 0; bottom: 28px; height: 36px;
    background: var(--band-grey);
    display: flex; align-items: center; gap: 10px; padding-left: 24px;
    color: #fff; font-size: 15px;
  }
</style>
</head>
<body>

<section class="card card-front">
  <div class="front-wordmark">
    <span class="mark-dot"></span>
    <span class="firm-name">BRENNOX LEGAL CO.</span>
  </div>
  <div class="front-band"><span class="web">www.brennoxlegalco.com</span></div>
</section>

<section class="card card-back">
  <div class="back-square"></div>
  <div class="back-wordmark">
    <span class="mark-square"></span>
    BRENNOX<br>LEGAL CO.
  </div>
  <div class="back-divider"></div>

  <div class="contact">
    <div class="person">DANIEL MARLOW</div>
    <div class="role">Attorney at Law</div>
    <div class="row strong">
      <svg class="icon" viewBox="0 0 16 16"><circle cx="8" cy="8" r="8" fill="var(--accent)"/><path d="M5 4.5l1.5-.5 1 2-1 .8a5 5 0 002.7 2.7l.8-1 2 1-.5 1.5c-3.5 0-6.5-3-6.5-6.5z" fill="#fff"/></svg>
      310.555.0142
    </div>
    <div class="rule"></div>
    <div class="row">
      <svg class="icon" viewBox="0 0 16 16"><circle cx="8" cy="8" r="8" fill="var(--accent)"/><path d="M8 3.5a3 3 0 00-3 3c0 2.2 3 6 3 6s3-3.8 3-6a3 3 0 00-3-3z" fill="#fff"/><circle cx="8" cy="6.5" r="1.1" fill="var(--accent)"/></svg>
      <span>518 Alder Crest Avenue, Suite 310<br>Beverly Hills, CA 90210</span>
    </div>
    <div class="row strong">
      <svg class="icon" viewBox="0 0 16 16"><circle cx="8" cy="8" r="8" fill="var(--accent)"/><path d="M5 4.5l1.5-.5 1 2-1 .8a5 5 0 002.7 2.7l.8-1 2 1-.5 1.5c-3.5 0-6.5-3-6.5-6.5z" fill="#fff"/></svg>
      <span>T. 310.555.0187<br>F. 310.555.0163</span>
    </div>
    <div class="row">
      <svg class="icon" viewBox="0 0 16 16"><circle cx="8" cy="8" r="8" fill="var(--accent)"/><rect x="4" y="5" width="8" height="6" rx="1" fill="#fff"/><path d="M4.3 5.4L8 8.3l3.7-2.9" stroke="var(--accent)" stroke-width="1" fill="none"/></svg>
      daniel@brennoxlegalco.com
    </div>
  </div>

  <div class="back-band">
    <svg class="icon" viewBox="0 0 16 16"><circle cx="8" cy="8" r="7" fill="#fff"/><g stroke="var(--band-grey)" stroke-width="1" fill="none"><circle cx="8" cy="8" r="5"/><ellipse cx="8" cy="8" rx="2.2" ry="5"/><path d="M3 8h10"/></g></svg>
    www.brennoxlegalco.com
  </div>
</section>

</body>
</html>
```